Medical Clinic Group Looking for Website Design

We own and operate medical clinics and are looking looking to revamp our website. Our current website is www.brightharborcare.ca We need our website to be more functional, user friendly, and easier to maintain.

```html
<!DOCTYPE html>
<html lang="en">
<head>
<meta charset="utf-8">
<title>Bright Harbor Care</title>
<link href="https://fonts.googleapis.com/css2?family=Jost:wght@300;400;500&display=swap" rel="stylesheet">
<style>
:root{
  --teal:#3ccfd8;
  --teal-dark:#2fbac3;
  --ink:#555;
  --ink-soft:#777;
  --btn:#6c6c6c;
  --line:#dcdcdc;
  --gray-bg:#f0f0f0;
  --footer:#6d6d6d;
  --footer-bar:#5d5d5d;
  --white:#fff;
}
*{box-sizing:border-box;margin:0;padding:0}
html,body{width:1200px;height:4019px;overflow:hidden}
body{font-family:'Jost',sans-serif;color:var(--ink);background:var(--white);position:relative}
section,header,footer{position:absolute;left:0;width:1200px}
.abs{position:absolute}
.btn{position:absolute;display:flex;align-items:center;justify-content:center;font-size:11px;font-weight:500;color:#fff;background:var(--btn);border-radius:3px;box-shadow:0 2px 4px rgba(0,0,0,.15);white-space:nowrap}
.btn--teal{background:var(--teal)}
.eyebrow{position:absolute;color:var(--teal);font-size:15px;font-weight:400;white-space:nowrap}
.heading{position:absolute;font-weight:300;color:#555;font-size:31px;line-height:36px}
.body-copy{position:absolute;font-size:10.5px;line-height:18.5px;color:var(--ink-soft)}

/* header */
.site-header{top:0;height:75px;background:#fff;box-shadow:0 1px 6px rgba(0,0,0,.06);z-index:2}
.brand{position:absolute;display:flex;align-items:center;gap:10px;font-size:26px;font-weight:400;color:var(--teal);white-space:nowrap}
.brand__dot{width:30px;height:30px;border-radius:50%;border:2px solid #8a8a8a;flex:none}
.nav{position:absolute;font-size:11px;color:#666}
.nav span{position:absolute;white-space:nowrap}

/* hero */
.hero{top:75px;height:499px;background:linear-gradient(120deg,#f3f3f3 0%,#e9e9e9 60%,#f4f4f4 100%)}
.photo{background:linear-gradient(135deg,#dfe6ea,#b8c6cf 55%,#f2d9b8)}

/* features */
.features{top:574px;height:401px;background:#fff}
.feature{position:absolute;width:274px;height:168px;text-align:center;font-size:14px;color:#666}
.feature svg{display:block;margin:36px auto 14px;width:48px;height:48px;stroke:var(--teal);fill:none;stroke-width:1.6;stroke-linecap:round;stroke-linejoin:round}
.feature--active{box-shadow:0 4px 14px rgba(0,0,0,.12);background:#fff;color:var(--teal)}
.vline{position:absolute;width:1px;background:var(--line)}
.hline{position:absolute;height:1px;background:var(--line)}

/* diamonds */
.diamond{position:absolute;transform:rotate(45deg);border-radius:26px;overflow:hidden}
.diamond-outline{position:absolute;transform:rotate(45deg);border-radius:26px;border:2px solid #c9c9c9}

.sports{top:975px;height:442px;background:linear-gradient(90deg,#f6f7f8,#fbfbfb 50%,#f4f6f7)}
.booking{top:1417px;height:440px;background:var(--gray-bg)}
.exciting{top:1857px;height:437px;background:#fff}

/* locations */
.locations{top:2294px;height:468px;background:var(--gray-bg)}
.section-title{position:absolute;width:1200px;text-align:center;font-size:29px;font-weight:300;color:#555}
.loc-card{position:absolute;width:225px;text-align:center}
.loc-card__img{height:157px;border-radius:0 40px 0 40px;box-shadow:4px 4px 0 #d8d8d8}
.loc-card__name{margin-top:26px;font-size:14px;color:#666}
.loc-card__sub{margin-top:4px;font-size:10.5px;color:var(--teal)}

/* articles */
.articles{top:2762px;height:601px;background:#fff}
.article-item{position:absolute;left:637px;width:362px;height:116px;border-bottom:1px solid var(--line)}
.article-item__thumb{position:absolute;left:0;top:8px;width:105px;height:105px}
.article-date{font-size:10px;color:var(--teal)}
.article-title{font-size:14.5px;line-height:22px;color:#555;margin-top:8px}

/* newsletter */
.newsletter{top:3363px;height:277px;background:var(--teal);color:#fff;text-align:center}
.newsletter input{position:absolute;left:354px;top:178px;width:381px;height:36px;border:none;padding-left:16px;font-family:inherit;font-size:11px;color:#888;background:#fff}

/* footer */
.site-footer{top:3640px;height:338px;background:var(--footer);color:#f1f1f1}
.foot-brand{position:absolute;left:106px;top:72px;display:flex;align-items:center;gap:10px;color:var(--teal);font-size:19px;line-height:22px;width:200px}
.foot-col{position:absolute;top:83px}
.foot-col h4{font-size:15px;font-weight:400;margin-bottom:16px}
.foot-col li{list-style:none;font-size:10.5px;line-height:22.5px;white-space:nowrap}
.contact-row{display:flex;align-items:center;gap:8px;font-size:12px;line-height:22px}
.contact-row svg{width:11px;height:11px;stroke:var(--teal);fill:none;stroke-width:2}
.foot-note{margin-top:12px;font-size:9px;line-height:18.5px;width:185px}
.social{position:absolute;left:1064px;width:24px;height:24px;border:1.5px solid var(--teal);transform:rotate(45deg);border-radius:3px}
.social--on{background:var(--teal)}
.foot-bar{position:absolute;top:3978px;left:0;width:1200px;height:41px;background:var(--footer-bar);color:#eee;font-size:9.5px;display:flex;align-items:center;justify-content:center;gap:16px}
</style>
</head>
<body>

<header class="site-header">
  <div class="brand" style="left:106px;top:20px"><span class="brand__dot"></span>Bright Harbor Care</div>
  <nav class="nav" style="left:0;top:30px">
    <span style="left:582px">Locations</span>
    <span style="left:666px">For Patients ⌄</span>
    <span style="left:774px">For Providers ⌄</span>
    <span style="left:889px">About Us ⌄</span>
  </nav>
  <div class="btn btn--teal" style="left:981px;top:19px;width:113px;height:36px;font-size:11.5px">Book Online</div>
</header>

<section class="hero">
  <div class="eyebrow" style="left:106px;top:146px">Bright Harbor Care</div>
  <h1 class="heading" style="left:106px;top:166px;font-size:31px;white-space:nowrap">We simplify providing care</h1>
  <p class="body-copy" style="left:106px;top:215px;width:385px;color:#6a6a6a;font-size:10px;line-height:15.5px">Through our years of experience working with healthcare providers, we have developed customizable practice management solutions that are proven to substantially reduce practice overhead and administrative burden; increase provider and patient satisfaction; and remove the added pressure of managing a business and employees.</p>
  <div class="btn" style="left:106px;top:314px;width:112px;height:36px">About Us</div>
  <div class="abs photo" role="img" aria-label="Hands of a doctor with stethoscope typing on a tablet showing health data" style="left:613px;top:112px;width:481px;height:275px"></div>
</section>

<section class="features">
  <div class="feature" style="left:200px;top:63px">
    <svg viewBox="0 0 48 48"><circle cx="18" cy="16" r="7"/><path d="M5 40c0-8 6-13 13-13s13 5 13 13"/><circle cx="32" cy="14" r="6"/><path d="M34 25c6 1 10 6 10 13"/></svg>Find a Provider</div>
  <div class="feature feature--active" style="left:463px;top:63px">
    <svg viewBox="0 0 48 48"><path d="M24 40S6 29 6 17a9 9 0 0 1 18-2 9 9 0 0 1 18 2c0 12-18 23-18 23z"/><path d="M14 22h6l3-5 4 9 3-4h5"/></svg>Services</div>
  <div class="feature" style="left:737px;top:63px">
    <svg viewBox="0 0 48 48"><rect x="6" y="9" width="36" height="32" rx="2"/><path d="M6 17h36M15 5v8M33 5v8"/><path d="M12 23h4M20 23h4M28 23h4M12 29h4M20 29h4M28 29h4M12 35h4M20 35h4"/></svg>Book an Appointment</div>
  <div class="hline" style="left:200px;top:231px;width:799px"></div>
  <div class="vline" style="left:463px;top:231px;height:170px"></div>
  <div class="vline" style="left:737px;top:231px;height:170px"></div>
  <div class="feature" style="left:200px;top:245px">
    <svg viewBox="0 0 48 48"><path d="M24 32S14 22 14 15a10 10 0 0 1 20 0c0 7-10 17-10 17z"/><circle cx="24" cy="15" r="4"/><path d="M14 30l-8 12h36l-8-12"/></svg>Locations</div>
  <div class="feature" style="left:463px;top:245px">
    <svg viewBox="0 0 48 48"><rect x="5" y="8" width="38" height="26" rx="2"/><path d="M18 42h12M24 34v8M11 15h16M11 21h12M11 27h8"/><rect x="30" y="15" width="8" height="12"/></svg>Patient Resources</div>
  <div class="feature" style="left:737px;top:245px">
    <svg viewBox="0 0 48 48"><path d="M10 6l7 8-4 5c2 5 7 10 12 12l5-4 8 7-4 6C20 40 8 28 6 12z"/><rect x="26" y="6" width="16" height="11" rx="3"/><path d="M30 17l-2 4 5-4"/></svg>Contact Us</div>
</section>

<section class="sports">
  <div class="diamond-outline" style="left:302px;top:122px;width:200px;height:200px"></div>
  <div class="diamond photo" role="img" aria-label="Clinician examining a patient's knee" style="left:282px;top:123px;width:200px;height:200px;background:linear-gradient(135deg,#e8d4c4,#5a5a5a 60%,#d6d6d6)"></div>
  <div class="eyebrow" style="left:613px;top:90px;font-size:14px">Your partner in health</div>
  <h2 class="heading" style="left:613px;top:110px;width:345px">Sports medicine services now available at our Pandosy location</h2>
  <p class="body-copy" style="left:613px;top:228px;width:385px">Bright Harbor Care is continually adding and improving our services to provide patients with access to comprehensive care under one roof. Speak with your healthcare provider about how interventional MSK treatments and regenerative therapy can help you today!</p>
  <div class="btn" style="left:613px;top:323px;width:180px;height:36px">Download Referral Form</div>
</section>

<section class="booking">
  <div class="eyebrow" style="left:200px;top:83px;font-size:14px">Easy access to care when you need it</div>
  <h2 class="heading" style="left:200px;top:103px;width:345px">Online appointment booking now available to all patients</h2>
  <p class="body-copy" style="left:200px;top:222px;width:390px">Bright Harbor Care continues to create options that better suit your lifestyle. Book your appointment when it's convenient for you, even if you don't have a family doctor.</p>
  <div class="btn" style="left:200px;top:318px;width:175px;height:36px">Book at Ridgeview Medical</div>
  <div class="btn btn--teal" style="left:387px;top:318px;width:112px;height:36px">Locations</div>
  <div class="diamond-outline" style="left:715px;top:156px;width:200px;height:200px"></div>
  <div class="diamond photo" role="img" aria-label="Hands typing on a laptop keyboard by a window" style="left:715px;top:106px;width:200px;height:200px;background:linear-gradient(135deg,#e4e8ea,#6b7176 55%,#2f3336)"></div>
</section>

<section class="exciting">
  <div class="diamond-outline" style="left:279px;top:118px;width:200px;height:200px"></div>
  <div class="diamond photo" role="img" aria-label="Smiling healthcare professional in a white coat" style="left:309px;top:118px;width:200px;height:200px;background:linear-gradient(135deg,#f1f1f1,#d8cabd 55%,#b8a596)"></div>
  <div class="eyebrow" style="left:613px;top:100px;font-size:14px">We're renovating to serve you better</div>
  <h2 class="heading" style="left:613px;top:120px;width:300px">Exciting things are happening!</h2>
  <p class="body-copy" style="left:613px;top:200px;width:385px">Bright Harbor Care is continually adding and improving our services to provide patients with access to comprehensive care under one roof. Speak with your healthcare provider about how interventional MSK treatments and regenerative therapy can help you today!</p>
  <div class="btn" style="left:613px;top:300px;width:124px;height:36px">Book Online</div>
</section>

<section class="locations">
  <h2 class="section-title" style="top:56px">Find a location near you</h2>
  <div class="loc-card" style="left:209px;top:116px">
    <div class="loc-card__img" role="img" aria-label="Blue clinic building exterior under cloudy sky" style="background:linear-gradient(180deg,#c9ced3 0%,#2c5a9a 45%,#8f8f8f 100%)"></div>
    <div class="loc-card__name">Kelowna - Glenmore</div>
    <div class="loc-card__sub">(Ridgeview Medical Clinic)</div>
  </div>
  <div class="loc-card" style="left:484px;top:116px">
    <div class="loc-card__img" role="img" aria-label="Clinic storefront with glass windows" style="background:linear-gradient(180deg,#5c6266,#2b3033 50%,#9aa0a3)"></div>
    <div class="loc-card__name">Kelowna - Pandosy</div>
    <div class="loc-card__sub">(Sports Medicine and Physiotherapy)</div>
  </div>
  <div class="loc-card" style="left:759px;top:116px">
    <div class="loc-card__img" role="img" aria-label="Single-storey clinic building with garden path" style="background:linear-gradient(180deg,#8da3b3,#3f4a3b 50%,#b4a891)"></div>
    <div class="loc-card__name">Kelowna - Springfield</div>
    <div class="loc-card__sub">(Summit Medical Group)</div>
  </div>
  <div class="btn btn--teal" style="left:537px;top:370px;width:125px;height:34px">View All Locations</div>
</section>

<section class="articles">
  <h2 class="section-title" style="top:56px">Recent articles</h2>
  <div class="abs" role="img" aria-label="Doctor examining a patient's knee" style="left:200px;top:123px;width:387px;height:236px;background:linear-gradient(135deg,#f0f0f0,#cfcfcf 50%,#3c3f4a)"></div>
  <div class="abs article-date" style="left:200px;top:390px">September 1, 2022</div>
  <div class="abs" style="left:200px;top:410px;width:387px;font-size:14.5px;line-height:22px;color:#555">Lorem Ipsum is simply dummy text of the printing and typesetting industry.</div>

  <div class="hline" style="left:637px;top:124px;width:362px"></div>
  <div class="article-item" style="top:124px">
    <div class="article-item__thumb" role="img" aria-label="Patient talking with a clinician" style="background:linear-gradient(135deg,#eee,#c6a9b4)"></div>
    <div class="abs" style="left:128px;top:22px;width:220px"><div class="article-date">October 20, 2022</div><div class="article-title">Lorem Ipsum is simply dummy text of the printing.</div></div>
  </div>
  <div class="article-item" style="top:240px">
    <div class="article-item__thumb" role="img" aria-label="Digital medical technology concept in blue" style="background:linear-gradient(135deg,#bde4f0,#2d7ea3)"></div>
    <div class="abs" style="left:128px;top:22px;width:220px"><div class="article-date">October 20, 2022</div><div class="article-title">Lorem Ipsum is simply dummy text of the printing.</div></div>
  </div>
  <div class="article-item" style="top:356px">
    <div class="article-item__thumb" role="img" aria-label="Two clinicians reviewing a tablet together" style="background:linear-gradient(135deg,#e9e9e9,#6e5a4d)"></div>
    <div class="abs" style="left:128px;top:22px;width:220px"><div class="article-date">October 20, 2022</div><div class="article-title">Lorem Ipsum is simply dummy text of the printing.</div></div>
  </div>
  <div class="btn" style="left:545px;top:504px;width:111px;height:36px">View All</div>
</section>

<section class="newsletter">
  <h2 class="abs" style="top:62px;width:1200px;font-size:30px;font-weight:300">Subscribe to our newsletter</h2>
  <p class="abs" style="top:114px;left:300px;width:600px;font-size:13.5px;line-height:23px;font-weight:300">Bright Harbor Care is focused on our patients first. Connect with us to stay up to date with current news and upcoming events.</p>
  <input type="text" placeholder="Enter your email ...">
  <div class="btn" style="left:735px;top:178px;width:111px;height:36px;border-radius:0 3px 3px 0">Subscribe</div>
</section>

<footer class="site-footer">
  <div class="foot-brand"><span class="brand__dot" style="border-color:#e3e3e3"></span><span>Bright Harbor<br>Care</span></div>
  <div class="foot-col" style="left:337px">
    <h4>Locations</h4>
    <ul><li>Kelowna - Glenmore</li><li>Kelowna - Pandosy</li><li>Kelowna - Springfield</li><li>Valley Women's Clinic</li><li>Lake Country</li></ul>
  </div>
  <div class="foot-col" style="left:546px">
    <h4>Contact us</h4>
    <div class="contact-row"><svg viewBox="0 0 12 12"><path d="M2 1l2 2-1 2c1 2 2 3 4 4l2-1 2 2-1 2C5 12 0 7 0 2z"/></svg>250.555.0142</div>
    <div class="contact-row" style="font-size:11px"><svg viewBox="0 0 12 12"><rect x="1" y="2" width="10" height="8"/><path d="M1 2l5 4 5-4"/></svg>hello@brightharborcare.ca</div>
    <p class="foot-note">Please do not send medical questions to this email. If you have a medical question, contact your doctor's office directly. Visit our locations page or <u>click here</u> to find contact information for each of our locations.</p>
  </div>
  <div class="foot-col" style="left:800px">
    <h4>Book online</h4>
    <ul><li>Kelowna - Glenmore (Ridgeview Medical)</li><li>Kelowna - Pandosy</li><li>Lake Country (Lakeshore Medical)</li></ul>
  </div>
  <div class="social" role="img" aria-label="Social link" style="top:82px"></div>
  <div class="social social--on" role="img" aria-label="Social link" style="top:126px"></div>
  <div class="social" role="img" aria-label="Social link" style="top:170px"></div>
</footer>
<div class="foot-bar"><span>©2021 Bright Harbor Care. All Right Reserved</span><span>|</span><span>Legal</span><span>|</span><span>Privacy Policy</span></div>

</body>
</html>
```